New Company Business Card Design

I have a new company logo and I want a new business card design. I dont know if the logo file i attached is in the correct format or quality. We are a New York City Specialty construction Firm specializing in high risk out of the box projects. I want a simple and classy business card that people will his card is as crisp as the work his company does.

Target Market(s)

Clients in the heavy construction industry in New York City

Industry/Entity Type

Construction Company

Contact Information for Business Card

Simple Classy - DIFFERENT

Font styles to use
Other font styles liked:
• Mach the logo font in some way

Colors

Designer to choose colors to be used in the design.

Requirements
Must have
• Uniqueness
Nice to have
• Nothing particular - Just different and classy - Timeless
Should not have
• Goofy Shit or Gimmicky shit

```html
<!DOCTYPE html>
<html lang="en">
<head>
<meta charset="utf-8">
<title>Keystone Rigging, Inc. – Business Card</title>
<link href="https://fonts.googleapis.com/css2?family=Roboto:wght@400;700&display=swap" rel="stylesheet">
<style>
  :root {
    --backdrop: #2b2b2d;
    --brand-navy: #1a4a92;
    --brand-sky: #1d8fdb;
    --card-white: #ffffff;
    --ink-grey: #4a4a4a;
  }
  * { margin: 0; padding: 0; box-sizing: border-box; }
  html, body {
    width: 1200px; height: 930px; overflow: hidden;
    background: var(--backdrop);
    font-family: "Roboto", Arial, sans-serif;
  }
  .canvas { position: relative; width: 1200px; height: 930px; }

  .card {
    position: absolute; width: 560px; height: 320px;
    border-radius: 14px; overflow: hidden;
    box-shadow: 0 10px 30px rgba(0,0,0,.45);
  }
  .card-front { left: 90px; top: 110px; background: var(--brand-navy); }
  .card-back  { left: 550px; top: 500px; background: var(--card-white); }

  .wordmark {
    display: flex; align-items: center; gap: 12px;
    font-weight: 700; letter-spacing: 1px; white-space: nowrap;
  }
  .wordmark-square { width: 18px; height: 18px; flex: none; }

  .card-front .wordmark {
    position: absolute; left: 50%; top: 50%; transform: translate(-50%, -50%);
    color: var(--card-white); font-size: 30px;
  }
  .card-front .wordmark-square { background: var(--card-white); }

  .card-back .wordmark {
    position: absolute; left: 36px; top: 124px;
    color: var(--brand-navy); font-size: 20px;
  }
  .card-back .wordmark-square { background: var(--brand-navy); width: 14px; height: 14px; }

  .person { position: absolute; right: 36px; top: 46px; text-align: right; }
  .person-name { color: var(--brand-sky); font-size: 27px; font-weight: 400; letter-spacing: .5px; }
  .person-title { color: var(--ink-grey); font-size: 13px; margin-top: 2px; }
  .person-rule { position: absolute; right: 36px; top: 108px; width: 190px; height: 2px; background: var(--brand-sky); }

  .address {
    position: absolute; right: 36px; top: 140px; text-align: right;
    color: var(--ink-grey); font-size: 13px; line-height: 1.45; font-style: normal;
  }

  .contact-rule { position: absolute; left: 36px; top: 214px; width: 240px; height: 2px; background: var(--brand-sky); }
  .contact-list {
    position: absolute; left: 36px; top: 224px; list-style: none;
    color: var(--ink-grey); font-size: 13px; line-height: 1.55;
  }
  .contact-list li { display: flex; align-items: center; gap: 8px; }
  .contact-list svg { width: 11px; height: 11px; flex: none; }
  .contact-list .highlight { color: var(--brand-sky); }

  .wave { position: absolute; left: 0; bottom: 0; width: 560px; height: 320px; }
</style>
</head>
<body>
<main class="canvas">

  <section class="card card-front" aria-label="Card front">
    <div class="wordmark"><span class="wordmark-square"></span>KEYSTONE RIGGING, INC.</div>
  </section>

  <section class="card card-back" aria-label="Card back">
    <svg class="wave" viewBox="0 0 560 320" aria-hidden="true">
      <path d="M0,296 L330,296 C352,296 356,262 384,262 L560,262 L560,320 L0,320 Z" fill="var(--brand-navy)"/>
      <path d="M0,290 L326,290 C346,290 350,258 372,256" fill="none" stroke="var(--brand-sky)" stroke-width="3"/>
      <path d="M0,308 L560,308" fill="none" stroke="var(--brand-sky)" stroke-width="3"/>
    </svg>

    <div class="wordmark"><span class="wordmark-square"></span>KEYSTONE RIGGING, INC.</div>

    <div class="person">
      <div class="person-name">COLIN MARSH</div>
      <div class="person-title">Director</div>
    </div>
    <div class="person-rule"></div>

    <address class="address">
      48 Harbor Ave.<br>Linden, NJ 07036
    </address>

    <div class="contact-rule"></div>
    <ul class="contact-list">
      <li>
        <svg viewBox="0 0 12 12"><path d="M2.5 1 L4.5 1 L5.2 3.5 L4 4.6 C4.7 6 6 7.3 7.4 8 L8.5 6.8 L11 7.5 L11 9.5 C11 10.3 10.3 11 9.5 11 C5 11 1 7 1 2.5 C1 1.7 1.7 1 2.5 1 Z" fill="var(--brand-sky)"/></svg>
        (555) 014-2290
      </li>
      <li>
        <svg viewBox="0 0 12 12"><rect x="1" y="2.5" width="10" height="7" fill="none" stroke="var(--brand-sky)" stroke-width="1.2"/><path d="M1 2.5 L6 6.5 L11 2.5" fill="none" stroke="var(--brand-sky)" stroke-width="1.2"/></svg>
        info@keystonerigging.com
      </li>
      <li>
        <svg viewBox="0 0 12 12"><circle cx="6" cy="6" r="5" fill="none" stroke="var(--brand-sky)" stroke-width="1.1"/><ellipse cx="6" cy="6" rx="2.2" ry="5" fill="none" stroke="var(--brand-sky)" stroke-width="1"/><path d="M1 6 H11" stroke="var(--brand-sky)" stroke-width="1"/></svg>
        <span>www.<span class="highlight">keystonerigging</span>.com</span>
      </li>
    </ul>
  </section>

</main>
</body>
</html>
```